Website Design for PawRank - New Digital Agency

We are creating a new digital marketing agency and need a new website. I have attached the logo. Our niche is going to be veterinarians. Use the same colors as in the logo (blue, white and gray).

I want real pictures of real people in this and not just boring stock photos. It needs to be related to the industry.

Home page (example:https://trellmarsh.com/)
Service page (example: https://dovequist.com/consulting/)
Case study page (example: https://www.harlowfinchley.com/seo/case-study/)

I will continue to update this brief.
Updates

I updated the brief with some additional sample sites 2 days ago and want to see more designs. I won't need that may more days ...just a few more.

Target Market(s)

veterinarians

Font styles to use
Sans Serif

Requirements
Must have
• I want a very clean looking site. Use the same colors as in the logo (blue, white and gray).
Nice to have
• We need to build this with the idea that the purpose is to generate leads for our business.
• Home page (example:https://trellmarsh.com/)
• Service page (example: https://dovequist.com/consulting/)
• Case study page (example: https://www.harlowfinchley.com/seo/case-study/)

```html
<!DOCTYPE html>
<html lang="en">
<head>
<meta charset="utf-8">
<title>PawRank – Digital Marketing for Veterinarians</title>
<link rel="stylesheet" href="https://fonts.googleapis.com/css2?family=Montserrat:wght@900&family=Oswald:wght@500&family=Raleway:ital,wght@0,400;0,500;0,600;0,700;1,400;1,500&display=swap">
<style>
:root{
  --blue:#0c56a6;
  --blue-deep:#0a4c95;
  --ink:#1f1f1f;
  --text:#3a3a3a;
  --muted:#7a7a7a;
  --line:#dcdcdc;
  --soft:#efefef;
  --white:#ffffff;
  --footer:#1b1b1b;
  --footer-text:#b9b9b9;
}
*{margin:0;padding:0;box-sizing:border-box}
html,body{width:1200px;height:3547px;overflow:hidden}
body{position:relative;font-family:"Raleway",sans-serif;color:var(--text);background:var(--white)}
.abs{position:absolute}
a{color:inherit;text-decoration:none}

/* header */
.hero-photo{left:0;top:0;width:1200px;height:677px;
  background:linear-gradient(180deg,#e6e7e8 0%,#dfe0e1 55%,#b9aea3 78%,#7d6a5a 100%)}
.brand{left:77px;top:22px;font:700 38px/1 "Raleway",sans-serif;color:var(--blue);display:flex;align-items:center;gap:10px}
.brand-dot{width:20px;height:20px;border-radius:50%;background:var(--blue)}
.nav a{position:absolute;top:32px;font:500 16px/1 "Raleway",sans-serif;color:var(--ink)}
.nav a.active{color:var(--blue)}
.nav-underline{left:650px;top:80px;width:55px;height:3px;background:var(--blue)}
.header-line{left:77px;top:82px;width:1046px;height:1px;background:#cfd0d1}
.btn-signup{left:1018px;top:21px;width:105px;height:41px;border-radius:4px;background:var(--blue);color:#fff;font:700 16px/41px "Raleway",sans-serif;text-align:center}

.hero-title{left:74px;top:245px;font:900 82px/80px "Montserrat",sans-serif;color:#111;letter-spacing:-1px}
.hero-sub{left:77px;top:422px;font:500 23px/1 "Oswald",sans-serif;color:var(--blue);letter-spacing:-.3px}
.btn-start{left:77px;top:466px;width:178px;height:53px;border-radius:3px;background:var(--blue);color:#fff;font:700 18px/53px "Raleway",sans-serif;text-align:center}

/* features */
.features{left:0;top:677px;width:1200px;height:239px;background:var(--blue)}
.feature{position:absolute;top:45px;width:220px;margin-left:-110px;text-align:center;color:#fff;font:600 17px/25px "Raleway",sans-serif}
.feature svg{display:block;margin:0 auto 22px;width:64px;height:64px;fill:none;stroke:#fff;stroke-width:2;stroke-linecap:round;stroke-linejoin:round}

/* section headings */
.section-title{font:700 44px/1 "Raleway",sans-serif;color:var(--ink)}
.section-title span{color:var(--blue)}

/* services */
.service{position:absolute;top:1068px;width:320px}
.service-icon{width:114px;height:114px;border-radius:50%;background:var(--soft);display:flex;align-items:center;justify-content:center}
.service-icon svg{width:62px;height:62px;fill:none;stroke:var(--blue);stroke-width:2;stroke-linecap:round;stroke-linejoin:round}
.service h3{margin-top:46px;font:600 19px/1 "Raleway",sans-serif;color:var(--blue)}
.service p{margin-top:22px;font:400 14px/27px "Raleway",sans-serif;color:var(--muted)}
.service .read{display:inline-block;margin-top:22px;font:600 14px/1 "Raleway",sans-serif;color:#444;text-decoration:underline}

/* welcome */
.welcome{left:0;top:1437px;width:1200px;height:624px;background:var(--blue)}
.welcome h2{position:absolute;left:80px;top:68px;font:700 44px/1 "Raleway",sans-serif;color:#fff}
.welcome .lead{position:absolute;left:79px;top:133px;width:500px;font:500 16px/29px "Raleway",sans-serif;color:#fff}
.welcome .body{position:absolute;left:79px;top:214px;width:500px;font:500 14px/27.5px "Raleway",sans-serif;color:#fff}
.btn-outline{position:absolute;border:1.5px solid #fff;border-radius:3px;color:#fff;text-align:center}
.btn-learn{left:77px;top:323px;width:167px;height:51px;font:700 16px/48px "Raleway",sans-serif}
.welcome-photo{position:absolute;left:654px;top:67px;width:469px;height:323px;
  background:linear-gradient(120deg,#6b5444 0%,#b9a78f 40%,#e7e2d6 70%,#cfc4b2 100%)}
.welcome-divider{position:absolute;left:77px;top:462px;width:1046px;height:1px;background:rgba(255,255,255,.25)}
.welcome .ask{position:absolute;left:222px;top:529px;font:600 20px/1 "Raleway",sans-serif;color:#fff}
.btn-phone{left:769px;top:517px;width:208px;height:51px;font:700 18px/48px "Raleway",sans-serif;display:flex;align-items:center;justify-content:center;gap:12px}
.btn-phone svg{width:24px;height:24px;fill:none;stroke:#fff;stroke-width:2;stroke-linecap:round;stroke-linejoin:round}

/* testimonials */
.quote-card{position:absolute;top:2202px;width:333px;height:217px;border:1px solid var(--line);border-radius:6px;background:#fff;padding:36px 22px 0 23px;font:italic 400 15px/29px "Raleway",sans-serif;color:#666}
.quote-card::after{content:"";position:absolute;left:40px;bottom:-12px;width:22px;height:22px;background:#fff;border-right:1px solid var(--line);border-bottom:1px solid var(--line);transform:rotate(45deg)}
.client{position:absolute;top:2458px;display:flex;align-items:center;gap:20px}
.client-photo{width:78px;height:78px;border-radius:50%;background:radial-gradient(circle at 50% 40%,#b8aca3 0%,#6f6a68 60%,#4a4a4c 100%)}
.client-name{font:700 16px/1 "Raleway",sans-serif;color:var(--blue)}
.client-site{margin-top:6px;font:400 14px/1 "Raleway",sans-serif;color:#444}

/* blog */
.blog-bg{left:0;top:2602px;width:1200px;height:541px;
  background:linear-gradient(90deg,#2a2d31 0%,#3b3f44 20%,#4e4a47 45%,#3d4046 70%,#2c2f33 100%)}
.blog-card{left:256px;top:2686px;width:688px;height:374px;background:#fff;text-align:center}
.blog-card h2{margin-top:58px;font:700 44px/1 "Raleway",sans-serif;color:var(--ink)}
.blog-card h2 span{color:var(--blue)}
.blog-meta{margin-top:31px;font:500 14px/1 "Raleway",sans-serif;color:var(--blue)}
.blog-head{margin-top:19px;font:700 17px/1 "Raleway",sans-serif;color:#222}
.blog-text{width:540px;margin:20px auto 0;font:400 14px/26px "Raleway",sans-serif;color:var(--muted)}
.arrow-btn{position:absolute;top:333px;width:67px;height:41px;background:var(--blue);display:flex;align-items:center;justify-content:center}
.arrow-btn svg{width:28px;height:16px;fill:none;stroke:#fff;stroke-width:2;stroke-linecap:round;stroke-linejoin:round}

/* footer */
.footer{left:0;top:3143px;width:1200px;height:404px;background:var(--footer)}
.footer h4{position:absolute;top:44px;font:600 18px/1 "Raleway",sans-serif;color:var(--blue)}
.footer-links{position:absolute;left:78px;top:92px;list-style:none}
.footer-links li{position:relative;padding-left:21px;font:500 15px/33.5px "Raleway",sans-serif;color:var(--footer-text)}
.footer-links li::before{content:"";position:absolute;left:0;top:14px;width:6px;height:6px;border-radius:50%;background:var(--blue)}
.contact-item{position:absolute;left:411px;display:flex;gap:19px;font:500 15px/25px "Raleway",sans-serif;color:var(--footer-text)}
.contact-item svg{flex:none;width:22px;height:22px;fill:var(--blue);margin-top:2px}
.btn-form{left:410px;top:242px;width:187px;height:46px;border-radius:3px;background:var(--blue);color:#fff;font:700 16px/46px "Raleway",sans-serif;text-align:center}
.about-text{position:absolute;left:755px;width:370px;font:500 14px/25px "Raleway",sans-serif;color:var(--footer-text)}
.footer-line{position:absolute;left:77px;top:338px;width:1046px;height:1px;background:#2f2f2f}
.copyright{position:absolute;left:78px;top:363px;font:400 13px/1 "Raleway",sans-serif;color:#8a8a8a}
.social{position:absolute;top:352px;width:37px;height:37px;border-radius:50%;background:#2c2c2c}
.social.active{border:2px solid var(--blue);background:#1b1b1b}
</style>
</head>
<body>

<!-- hero -->
<div class="abs hero-photo" role="img" aria-label="Photo of a black and white dog wearing a bandana, standing on lichen-covered rocks in morning fog"></div>

<div class="abs brand"><span>PawRank</span><span class="brand-dot"></span></div>
<nav class="nav">
  <a class="active" style="left:658px">Home</a>
  <a style="left:732px">About Us</a>
  <a style="left:834px">Services</a>
  <a style="left:926px">Contact</a>
</nav>
<div class="abs nav-underline"></div>
<div class="abs header-line"></div>
<a class="abs btn-signup">SIGN UP</a>

<h1 class="abs hero-title">WE BUILD<br>BRAND</h1>
<p class="abs hero-sub">DIGITAL MARKETING SOLUTION PAWRANK</p>
<a class="abs btn-start">GET STARTED</a>

<!-- features -->
<section class="abs features">
  <div class="feature" style="left:173px">
    <svg viewBox="0 0 64 64"><rect x="4" y="12" width="56" height="42" rx="3"/><path d="M4 20h56M16 12V7h14v5"/><circle cx="32" cy="33" r="11"/><path d="M28 37l8-8M27 33l-2 2a3 3 0 0 0 4 4l2-2M37 33l2-2a3 3 0 0 0-4-4l-2 2"/></svg>
    Relevant,<br>Powerful Links
  </div>
  <div class="feature" style="left:385px">
    <svg viewBox="0 0 64 64"><path d="M32 4v56"/><path d="M40 18c-2-4-5-5-8-5-5 0-9 3-9 7 0 10 18 6 18 16 0 5-4 8-9 8-4 0-8-2-10-6"/><path d="M26 4h12M26 60h12"/></svg>
    Reduce<br>Operational Costs
  </div>
  <div class="feature" style="left:599px">
    <svg viewBox="0 0 64 64"><rect x="6" y="8" width="52" height="36" rx="2"/><path d="M24 52h16M32 44v8"/><path d="M16 20l6 6M22 20l-6 6M30 18l4 8 4-8M42 32l8 8 4-4-8-8"/></svg>
    Only White<br>Hat Strategies
  </div>
  <div class="feature" style="left:810px">
    <svg viewBox="0 0 64 64"><path d="M12 34v-6a20 20 0 0 1 40 0v6"/><rect x="8" y="32" width="8" height="14" rx="3"/><rect x="48" y="32" width="8" height="14" rx="3"/><path d="M52 46c0 8-8 12-16 12h-4"/><path d="M14 60c4-6 10-8 18-8s14 2 18 8"/></svg>
    World-class<br>Customer Support
  </div>
  <div class="feature" style="left:1025px">
    <svg viewBox="0 0 64 64"><circle cx="24" cy="24" r="16"/><circle cx="42" cy="42" r="16"/></svg>
    100%<br>Satisfaction
  </div>
</section>

<!-- services -->
<h2 class="abs section-title" style="left:79px;top:978px">OUR <span>SERVICES</span></h2>

<article class="service" style="left:77px">
  <div class="service-icon"><svg viewBox="0 0 64 64"><rect x="14" y="6" width="36" height="30" rx="2"/><path d="M14 14h36M20 22h24M20 28h16"/><circle cx="22" cy="46" r="12"/><circle cx="22" cy="46" r="6"/><path d="M22 46l10-10M40 40v16h12V44l-6-2"/></svg></div>
  <h3>Paid Media</h3>
  <p>Lorem Ipsum is simply dummy text of the<br>printing and typesetting industry.</p>
  <a class="read">RAED MORE</a>
</article>
<article class="service" style="left:439px">
  <div class="service-icon"><svg viewBox="0 0 64 64"><rect x="10" y="4" width="44" height="56" rx="2"/><rect x="18" y="12" width="28" height="12"/><path d="M18 32h28M18 38h16M18 44h12M18 50h12"/><circle cx="44" cy="47" r="6"/></svg></div>
  <h3>Content Marketing Management</h3>
  <p>Lorem Ipsum is simply dummy text of the<br>printing and typesetting industry.</p>
  <a class="read">RAED MORE</a>
</article>
<article class="service" style="left:804px">
  <div class="service-icon"><svg viewBox="0 0 64 64"><rect x="24" y="4" width="16" height="20" rx="2"/><rect x="6" y="30" width="20" height="16" rx="2"/><path d="M13 34v8l6-4zM40 40l14-8v20l-14-6zM34 40h6v6h-6zM46 14a16 16 0 0 1 8 12M14 24a16 16 0 0 1 8-10M30 56a16 16 0 0 1-14-6"/></svg></div>
  <h3>Digital Services</h3>
  <p>Lorem Ipsum is simply dummy text of the<br>printing and typesetting industry.</p>
  <a class="read">RAED MORE</a>
</article>

<!-- welcome -->
<section class="abs welcome">
  <h2>Welcome To PawRank</h2>
  <p class="lead">Lorem Ipsum is simply dummy text of the printing and typesetting setting industry. Lorem Ipsum has been the.</p>
  <p class="body">Lorem Ipsum is simply dummy text of the printing and typesetting industry. Lorem Ipsum has been the industry's standard dummy text ever since the 1500s, when an unknown printer took a galley of type.</p>
  <a class="btn-outline btn-learn">LEARN MORE</a>
  <div class="welcome-photo" role="img" aria-label="Photo of a smiling veterinarian with a stethoscope holding a spaniel dog"></div>
  <div class="welcome-divider"></div>
  <p class="ask">If you Have an any Question For Contact Us Today !</p>
  <a class="btn-outline btn-phone"><svg viewBox="0 0 24 24"><path d="M5 3h4l2 5-3 2a12 12 0 0 0 6 6l2-3 5 2v4a2 2 0 0 1-2 2A18 18 0 0 1 3 5a2 2 0 0 1 2-2zM15 3a6 6 0 0 1 6 6M15 7a2 2 0 0 1 2 2"/></svg>123 456 7890</a>
</section>

<!-- testimonials -->
<h2 class="abs section-title" style="left:79px;top:2103px">OUR <span>TESTIMONIAL</span></h2>

<blockquote class="quote-card" style="left:77px">" Lorem Ipsum is simply dummy text of the printing and type setting since industry. Lorem Ipsum has been the industry's standard dummy text ever since the when an "</blockquote>
<blockquote class="quote-card" style="left:433px">" Lorem Ipsum is simply dummy text of the printing and type setting since industry. Lorem Ipsum has been the industry's standard dummy text ever since the when an "</blockquote>
<blockquote class="quote-card" style="left:790px">" Lorem Ipsum is simply dummy text of the printing and type setting since industry. Lorem Ipsum has been the industry's standard dummy text ever since the when an "</blockquote>

<div class="client" style="left:91px"><div class="client-photo" role="img" aria-label="Client portrait photo"></div><div><div class="client-name">CLIENT NAME</div><div class="client-site">something.com</div></div></div>
<div class="client" style="left:447px"><div class="client-photo" role="img" aria-label="Client portrait photo"></div><div><div class="client-name">CLIENT NAME</div><div class="client-site">something.com</div></div></div>
<div class="client" style="left:803px"><div class="client-photo" role="img" aria-label="Client portrait photo"></div><div><div class="client-name">CLIENT NAME</div><div class="client-site">something.com</div></div></div>

<!-- blog -->
<div class="abs blog-bg" role="img" aria-label="Darkened photo collage of laptops with analytics charts, office desks and business people"></div>
<article class="abs blog-card">
  <h2>LATEST <span>BLOG</span></h2>
  <p class="blog-meta">20 July 2019 &nbsp;|&nbsp; By PawRank</p>
  <h3 class="blog-head">Lorem Ipsum is simply text Dummy text industry.</h3>
  <p class="blog-text">Lorem Ipsum is simply dummy text of the printing and typesetting industry. Lorem Ipsum has been the industry's standard dummy text ever since the 1500s, when an unknown printer took a galley of type.</p>
  <a class="arrow-btn" style="left:0"><svg viewBox="0 0 28 16"><path d="M26 12V9a4 4 0 0 0-4-4H3M7 1L3 5l4 4"/></svg></a>
  <a class="arrow-btn" style="right:0"><svg viewBox="0 0 28 16"><path d="M2 12V9a4 4 0 0 1 4-4h19M21 1l4 4-4 4"/></svg></a>
</article>

<!-- footer -->
<footer class="abs footer">
  <h4 style="left:78px">QUICK LINKS</h4>
  <ul class="footer-links">
    <li>Home</li><li>About us</li><li>Services</li><li>Blog</li><li>Contact Us</li>
  </ul>

  <h4 style="left:412px">CONTACT INFO</h4>
  <div class="contact-item" style="top:88px"><svg viewBox="0 0 24 24"><path d="M12 1a8 8 0 0 0-8 8c0 6 8 14 8 14s8-8 8-14a8 8 0 0 0-8-8zm0 11a3 3 0 1 1 0-6 3 3 0 0 1 0 6z"/></svg><span>101 - Lorem ipsum simple text<br>of print type industry.</span></div>
  <div class="contact-item" style="top:157px"><svg viewBox="0 0 24 24"><path d="M5 2h4l2 5-3 2a12 12 0 0 0 6 6l2-3 5 2v4a2 2 0 0 1-2 2A18 18 0 0 1 3 4a2 2 0 0 1 2-2z"/></svg><span>+(1) 123 456 7890</span></div>
  <div class="contact-item" style="top:195px"><svg viewBox="0 0 24 24"><path d="M2 5h20v14H2z" fill-opacity=".001"/><path d="M2 5h20l-10 8zM2 7l10 8 10-8v12H2z"/></svg><span>info@PawRank.com</span></div>
  <a class="abs btn-form">REQUEST A FORM</a>

  <h4 style="left:756px">ABOUT US</h4>
  <p class="about-text" style="top:88px">Lorem Ipsum is simply dummy text of the printing and typesetting industry Ipsum has been.</p>
  <p class="about-text" style="top:154px">Lorem Ipsum is simply dummy text of the printing and typesetting industry. Lorem Ipsum has been the indus try's standard dummy text ever since the.</p>

  <div class="footer-line"></div>
  <p class="copyright">©PawRank - 2019 All Rights Reserved.</p>
  <span class="social" style="left:947px"></span>
  <span class="social active" style="left:992px"></span>
  <span class="social" style="left:1038px"></span>
  <span class="social" style="left:1084px"></span>
</footer>

</body>
</html>
```